Business Card Design

We need a business card design for a new company called Riverbend Advisory, LLC. We are a project management and software engineering consulting company. We prefer to use blues but am open to any colors. We would like out design to show strength and creativity.

I've uploaded new logo designs to the project.  Please use these logo designs for the business card. Thanks!

Industry/Entity Type

Software

Contact Information for Business Card

Daniel Whitford
Consultant
Owner

Riverbend Advisory, LLC

2716 5th St. S #4372
Arlington, VA 22198

703-555-0187
dwhitford@rvbadv.example
www.rvbadv.example

```html
<!DOCTYPE html>
<html lang="en">
<head>
<meta charset="utf-8">
<title>Riverbend Advisory – Business Cards</title>
<link href="https://fonts.googleapis.com/css2?family=Exo+2:wght@400;500;600&display=swap" rel="stylesheet">
<style>
  :root {
    --navy: #0b3a5c;
    --red: #b3372a;
    --paper: #ffffff;
    --ink-soft: #6b7177;
    --backdrop: #e9e6e1;
    --divider: #c9ccd0;
  }
  * { box-sizing: border-box; margin: 0; padding: 0; }
  html, body {
    width: 1200px; height: 848px; overflow: hidden;
    background: var(--backdrop);
    font-family: "Exo 2", sans-serif;
  }
  .canvas { position: relative; width: 1200px; height: 848px; }

  .card {
    position: absolute;
    width: 560px; height: 320px;
    box-shadow: 0 6px 18px rgba(0,0,0,0.18);
    overflow: hidden;
  }

  /* Front */
  .card-front { left: 60px; top: 60px; background: var(--paper); }
  .front-brand {
    position: absolute; left: 40px; top: 128px; width: 250px;
    display: flex; align-items: center; gap: 10px;
  }
  .brand-square { width: 16px; height: 16px; background: var(--navy); flex: none; }
  .brand-name {
    font-size: 23px; font-weight: 600; color: var(--navy);
    letter-spacing: 0.5px; line-height: 1.15;
  }
  .contact-block {
    position: absolute; left: 318px; top: 46px;
    padding-left: 18px; border-left: 1px solid var(--divider);
    height: 170px;
  }
  .contact-name { font-size: 15px; font-weight: 600; color: var(--navy); }
  .contact-role { font-size: 12px; color: var(--ink-soft); margin-top: 4px; }
  .contact-address { font-size: 12.5px; color: var(--ink-soft); margin-top: 18px; line-height: 1.5; }
  .contact-lines { margin-top: 14px; display: grid; grid-template-columns: 46px auto; row-gap: 3px; font-size: 12px; }
  .contact-label { font-weight: 600; color: var(--navy); }
  .contact-value { color: var(--ink-soft); }
  .front-stripe-red {
    position: absolute; left: 0; right: 0; bottom: 12px; height: 3px; background: var(--red);
  }
  .front-stripe-navy {
    position: absolute; left: 0; right: 0; bottom: 0; height: 9px; background: var(--navy);
  }

  /* Back */
  .card-back { left: 580px; top: 468px; background: var(--navy); }
  .back-brand {
    position: absolute; left: 0; right: 0; top: 138px;
    display: flex; justify-content: center; align-items: center; gap: 12px;
  }
  .back-brand .brand-square { background: var(--paper); }
  .back-brand .brand-name { color: var(--paper); font-size: 26px; }
  .back-web {
    position: absolute; right: 22px; bottom: 30px;
    writing-mode: vertical-rl; transform: rotate(180deg);
    font-size: 11px; letter-spacing: 7px; color: var(--paper);
  }
</style>
</head>
<body>
<main class="canvas">

  <section class="card card-front" aria-label="Business card front">
    <div class="front-brand">
      <span class="brand-square"></span>
      <span class="brand-name">Riverbend Advisory</span>
    </div>

    <div class="contact-block">
      <p class="contact-name">Daniel Whitford</p>
      <p class="contact-role">Consultant | Owner</p>
      <p class="contact-address">2716 5th St. S #4372<br>Arlington, VA 22198</p>
      <div class="contact-lines">
        <span class="contact-label">Phone:</span><span class="contact-value">703-555-0187</span>
        <span class="contact-label">Email:</span><span class="contact-value">dwhitford@rvbadv.example</span>
        <span class="contact-label">Web:</span><span class="contact-value">www.rvbadv.example</span>
      </div>
    </div>

    <div class="front-stripe-red"></div>
    <div class="front-stripe-navy"></div>
  </section>

  <section class="card card-back" aria-label="Business card back">
    <div class="back-brand">
      <span class="brand-square"></span>
      <span class="brand-name">Riverbend Advisory</span>
    </div>
    <p class="back-web">www.rvbadv.example</p>
  </section>

</main>
</body>
</html>
```